RW Stewardship real estate management company needs presentation folder to hand clients

looking for a folder with pockets that represent my real estate management company when i hand to client reports or promotional material. I only do resedential real estate. I want classy and professional - pictures or additioal graphixs are fine

when a client open i will usally insert text and reports about my business
also on the inside flap is usally place for my business card i will upload a picture so the theme can be constant

Target Market(s)

my existing real estate cleints
and i will use when i am soliciting new business

Industry/Entity Type

Real Estate

Font styles to use
Serif

Requirements
Must have
• must have logo
• must give appearance of professionalism and maturity
• have basic company info tel# ,address
• id like viewer to know I manage real estate - focus on residential small to large apartment buildings
• not strip malls, not giganic complexes - im a mid size company
• logo is black but i welcome color as u see fit
Nice to have
• maybe pictures
• my slogan - " we will manage your building like its our own "
• focus on professioanl, safe, trust worthy
• type style should be clear and readable - but im open to sugestions

```html
<!DOCTYPE html>
<html lang="en">
<head>
<meta charset="utf-8">
<title>RW Stewardship – Presentation Folder</title>
<link href="https://fonts.googleapis.com/css2?family=Arimo:wght@400;700&display=swap" rel="stylesheet">
<style>
  :root {
    --paper: #ffffff;
    --ink: #000000;
    --grey-dark: #5a5a5a;
    --grey-mid: #8c8c8c;
    --grey-light: #b4b4b4;
    --grey-pale: #e6e6e6;
    --text-grey: #555555;
    --photo-top: #3a3a3a;
    --photo-bottom: #a8a8a8;
    --dieline: #555555;
  }
  html, body {
    margin: 0;
    padding: 0;
    width: 1200px;
    height: 1200px;
    overflow: hidden;
    background: var(--paper);
  }
  .folder-flat {
    display: block;
    width: 1200px;
    height: 1200px;
    font-family: "Arimo", Arial, sans-serif;
  }
  .dieline { fill: none; stroke: var(--dieline); stroke-width: 1; }
  .ink { fill: var(--ink); }
  .grey-dark { fill: var(--grey-dark); }
  .grey-mid { fill: var(--grey-mid); }
  .grey-light { fill: var(--grey-light); }
  .grey-pale { fill: var(--grey-pale); }
  .paper { fill: var(--paper); }
  .brand-name { font-family: "Arimo", Arial, sans-serif; font-weight: 700; fill: var(--ink); }
  .contact-line { font-size: 14px; fill: var(--text-grey); }
  .slogan-text { font-size: 14px; fill: var(--paper); }
  .card-text { fill: var(--ink); }
</style>
</head>
<body>
<svg class="folder-flat" viewBox="0 0 1300 1300" xmlns="http://www.w3.org/2000/svg">
  <defs>
    <linearGradient id="cityTone" x1="0" y1="0" x2="0" y2="1">
      <stop offset="0" stop-color="var(--photo-top)"/>
      <stop offset="1" stop-color="var(--photo-bottom)"/>
    </linearGradient>
  </defs>

  <!-- Back cover panel -->
  <g class="panel back-cover">
    <polygon role="img" aria-label="Street view of residential apartment towers in the city" fill="url(#cityTone)"
             points="108,168 522,168 118,552 108,560"/>
    <polygon class="grey-light" points="300,168 360,168 160,520"/>
    <polygon class="grey-pale" points="440,168 470,168 200,480"/>
    <polygon class="ink" points="108,568 380,888 108,888"/>
    <polygon class="grey-dark" points="108,568 380,888 500,888"/>
    <polygon class="grey-mid" points="108,568 500,888 560,888"/>
    <polygon class="grey-light" points="108,568 560,888 648,888"/>

    <g class="brand-mark" transform="translate(455,528)">
      <rect class="ink" x="-104" y="-9" width="14" height="14"/>
      <text class="brand-name" x="10" y="5" font-size="22" text-anchor="middle">RW Stewardship</text>
    </g>
  </g>

  <!-- Front cover panel -->
  <g class="panel front-cover">
    <polygon role="img" aria-label="City avenue lined with apartment buildings" fill="url(#cityTone)"
             points="648,168 1188,168 920,462 648,330"/>
    <polygon class="ink" points="648,290 648,330 920,462"/>
    <polygon class="ink" points="1140,168 1188,168 1188,200 925,462"/>
    <polygon class="grey-light" points="1188,200 1188,230 930,462"/>

    <g class="brand-mark" transform="translate(917,590)">
      <rect class="ink" x="-104" y="-9" width="14" height="14"/>
      <text class="brand-name" x="10" y="5" font-size="22" text-anchor="middle">RW Stewardship</text>
    </g>

    <text class="contact-line" x="922" y="764" text-anchor="middle">Office: 555-210-4400 | Email: office@rwstewardship.com | Cell: 555-310-7720</text>
    <text class="contact-line" x="922" y="781" text-anchor="middle">42 Alder Court Suite 210, Brookfield NY 10990</text>

    <rect class="ink slogan-bar" x="648" y="797" width="540" height="32"/>
    <text class="slogan-text" x="918" y="818" text-anchor="middle">We will manage your building like it is our own</text>
  </g>

  <!-- Inside pocket flap, left: business card slot -->
  <g class="panel card-flap">
    <polygon class="grey-light" points="370,888 395,888 180,1128 150,1128"/>
    <polygon class="ink" points="345,888 372,888 150,1128 108,1128 108,1120"/>
    <polygon class="grey-mid" points="330,888 345,888 108,1110 108,1090"/>
    <polygon class="grey-pale" points="395,888 410,888 205,1128 180,1128"/>

    <g class="card-slot">
      <polyline class="dieline" points="608,932 632,932 632,956"/>
      <polyline class="dieline" points="392,1060 392,1084 416,1084"/>
    </g>

    <g class="business-card" transform="rotate(180 513 1008)">
      <polygon class="ink" points="400,940 626,940 626,1076 400,1076"/>
      <rect class="paper" x="410" y="950" width="206" height="116"/>
      <rect class="ink" x="410" y="958" width="6" height="100"/>
      <rect class="ink" x="610" y="958" width="6" height="100"/>
      <line x1="420" y1="955" x2="606" y2="955" stroke="var(--grey-mid)" stroke-width="0.6"/>
      <rect class="ink" x="424" y="979" width="6" height="6"/>
      <text class="brand-name" x="434" y="985" font-size="7">RW Stewardship</text>
      <line x1="507" y1="972" x2="507" y2="1040" stroke="var(--ink)" stroke-width="0.8"/>
      <text class="card-text" x="514" y="984" font-size="12" font-weight="700">Daniel Reyes</text>
      <text class="card-text" x="514" y="994" font-size="5.5">MASTER BUILDING MANAGER</text>
      <text class="card-text" x="514" y="1006" font-size="5.5">office  tel  555-210-4400</text>
      <text class="card-text" x="514" y="1014" font-size="5.5">cell  555-310-7720</text>
      <text class="card-text" x="514" y="1022" font-size="5.5">email  office@rwstewardship.com</text>
      <text class="card-text" x="514" y="1030" font-size="3.6">42 ALDER COURT SUITE 210 BROOKFIELD NY 10990</text>
      <line x1="420" y1="1048" x2="606" y2="1048" stroke="var(--grey-mid)" stroke-width="0.6"/>
      <text class="card-text" x="513" y="1057" font-size="4.5" text-anchor="middle">WE WILL MANAGE YOUR BUILDING LIKE IT IS OUR OWN</text>
    </g>
  </g>

  <!-- Inside pocket flap, right -->
  <g class="panel pocket-flap">
    <g class="brand-mark" transform="rotate(180 917 1000)">
      <rect class="ink" x="832" y="991" width="12" height="12"/>
      <text class="brand-name" x="925" y="1005" font-size="18" text-anchor="middle">RW Stewardship</text>
    </g>
  </g>

  <!-- Fold and cut lines -->
  <g class="dielines">
    <rect class="dieline" x="108" y="168" width="1080" height="960"/>
    <line class="dieline" x1="648" y1="168" x2="648" y2="1128"/>
    <line class="dieline" x1="108" y1="888" x2="1188" y2="888"/>
  </g>
</svg>
</body>
</html>
```